Jewelery Website

Please visit: http://www.lucastorvi.com/dev/wpnew/

Target Market(s)

Women between 25 and 44 years old

Number of Pages Required

5+ page

Font styles to use
Sans Serif
Script
Other font styles liked:
• Futura

Colors

Designer to choose colors to be used in the design.

```html
<!DOCTYPE html>
<html lang="en">
<head>
<meta charset="utf-8">
<title>Lucas Torvi Pearls</title>
<link rel="stylesheet" href="https://fonts.googleapis.com/css2?family=Jost:wght@400;500;600&family=Open+Sans:wght@400;700&family=Cormorant+Garamond:wght@500;600&family=Tinos:wght@400;700&display=swap">
<style>
:root{
  --ink:#2a2a2a;
  --topbar:#2b2b2b;
  --white:#ffffff;
  --nav:#e9edf2;
  --blue:#4a8fc9;
  --page:#eef2f8;
  --plum:#2e1a47;
  --price-plum:#3b2361;
  --green:#3bb58a;
}
*{box-sizing:border-box;margin:0;padding:0}
html,body{width:903px;height:1200px;overflow:hidden}
body{background:var(--page);font-family:"Jost",sans-serif;color:var(--ink);position:relative}
.topbar{position:absolute;left:0;top:0;width:903px;height:34px;background:var(--topbar);color:#e4e4e4;font-size:11.5px}
.topbar .left{position:absolute;left:53px;top:10px;display:flex;gap:10px}
.topbar .right{position:absolute;left:532px;top:10px;display:flex;gap:10px}
.sep{color:#aaa}
.header{position:absolute;left:0;top:34px;width:903px;height:88px;background:var(--white)}
.brand{position:absolute;left:351px;top:30px;width:200px;display:flex;align-items:center;justify-content:center;gap:8px;font-family:"Jost",sans-serif;font-weight:500;font-size:17px;letter-spacing:2px;color:var(--topbar)}
.brand .mark{width:10px;height:10px;background:var(--topbar)}
.shipping{position:absolute;left:60px;top:30px;display:flex;gap:8px;align-items:center}
.shipping .title{color:var(--blue);font-weight:600;font-size:11.5px;letter-spacing:-.2px}
.shipping .line{font-size:11px;color:#222}
.search{position:absolute;left:566px;top:26px;width:234px;height:26px;border:1px solid #cfd6de;background:#fff;display:flex}
.search span{flex:1;font-size:9.5px;color:#a5acb4;padding:7px 6px}
.search .btn{width:27px;background:var(--blue);display:flex;align-items:center;justify-content:center}
.cart{position:absolute;left:818px;top:26px}
.nav{position:absolute;left:0;top:122px;width:903px;height:38px;background:var(--nav);font-size:17px;color:#2d2d2d}
.nav .item{position:absolute;top:8px;display:flex;align-items:center;gap:5px}
.nav .active{color:var(--blue)}
.nav .bar{position:absolute;top:8px;color:#333}
.hero{position:absolute;left:0;top:160px;width:903px;height:432px;overflow:hidden}
.hero .wall{position:absolute;inset:0;background:linear-gradient(180deg,#a4a8ad 0%,#8e939a 55%,#7d8289 100%)}
.hero .model{position:absolute;left:430px;top:0;width:420px;height:432px;background:
  radial-gradient(ellipse 90px 120px at 200px 100px,#c99a82 0%,rgba(201,154,130,0) 100%),
  radial-gradient(ellipse 160px 110px at 230px 270px,#4c4a50 0%,rgba(76,74,80,0) 100%),
  radial-gradient(ellipse 230px 260px at 260px 380px,#f2f1f0 0%,rgba(242,241,240,0) 100%),
  linear-gradient(90deg,rgba(60,45,40,0) 0%,#4a3a33 35%,#6a5a52 60%,rgba(160,160,165,0) 100%)}
.hero h1{position:absolute;left:54px;font-family:"Open Sans",sans-serif;color:#fff;font-weight:400;font-size:40px;letter-spacing:-.5px}
.hero .l1{top:100px}
.hero .l2{top:156px;font-weight:700;font-size:39px}
.band{position:absolute;left:0;top:265px;width:420px;height:67px;background:var(--blue);display:flex;align-items:center;padding-left:74px;gap:14px;color:#fff;font-family:"Open Sans",sans-serif;font-size:25px}
.band-end{position:absolute;left:832px;top:265px;width:71px;height:67px;background:var(--blue)}
.reviews{position:absolute;left:0;top:592px;width:903px;height:48px;background:#fff;display:flex;align-items:center;justify-content:center;gap:22px;font-size:10.5px;letter-spacing:.6px}
.score{background:var(--green);color:#fff;font-size:9px;padding:1px 4px;margin-left:4px}
.reviews b{font-weight:600}
.partner{font-size:10.5px;font-weight:600;letter-spacing:.6px;color:#333}
.deals{position:absolute;left:56px;top:644px;width:794px;height:234px}
.deals .promo{position:absolute;left:0;top:0;width:330px;height:234px;background:var(--plum);color:#fff;text-align:center;font-family:"Cormorant Garamond",serif}
.promo .kicker{font-family:"Open Sans",sans-serif;font-size:13px;color:#ddd;margin-top:23px}
.promo .rule{width:188px;height:1px;background:#bbb;margin:9px auto 0}
.promo h2{font-size:42px;font-weight:600;font-variant:small-caps;line-height:.98;margin-top:8px;letter-spacing:1px}
.promo .note{font-size:15px;letter-spacing:.8px;line-height:1.15;margin-top:8px}
.promo .cta{display:inline-block;background:#fff;color:#222;font-family:"Open Sans",sans-serif;font-size:9px;padding:7px 24px;margin-top:12px}
.deals .showcase{position:absolute;left:330px;top:0;width:464px;height:234px;background:
  radial-gradient(ellipse 70px 70px at 130px 150px,#7fc6ea 0%,rgba(127,198,234,0) 100%),
  radial-gradient(ellipse 90px 60px at 270px 90px,#eef2f7 0%,rgba(238,242,247,0) 100%),
  radial-gradient(ellipse 80px 50px at 300px 190px,#f4f6fa 0%,rgba(244,246,250,0) 100%),
  linear-gradient(135deg,#dbe9f7 0%,#b9d3ee 55%,#a9c8ea 100%)}
.price{position:absolute;font-family:"Tinos",serif;color:var(--price-plum);font-weight:700;font-size:27px;line-height:1}
.price sup{font-size:13px;vertical-align:top;position:relative;top:2px}
.was{position:absolute;font-size:9.5px;color:#3a3a55}
.featured{position:absolute;left:53px;top:914px;width:797px;height:260px;background:#fff}
.featured h3{position:absolute;left:0;width:100%;top:22px;text-align:center;font-weight:400;font-size:25px;color:#333}
.product{position:absolute;top:58px;width:110px;text-align:center;font-family:"Tinos",serif;font-size:10px;color:#555}
.product .shot{width:80px;height:80px;margin:0 auto}
.shot.gold{background:radial-gradient(ellipse 34px 22px at 50% 60%,#e2c98a 0%,#f3ead2 60%,#fff 100%)}
.shot.silver{background:radial-gradient(ellipse 36px 30px at 50% 50%,#d6d9dd 0%,#eef0f2 60%,#fff 100%)}
.shot.black{background:radial-gradient(ellipse 36px 18px at 50% 55%,#2f3133 0%,#8a8c8e 60%,#fff 100%)}
.shot.rosegold{background:radial-gradient(ellipse 36px 30px at 50% 55%,#d9b98a 0%,#f1e4cd 60%,#fff 100%)}
.product .p{margin-top:33px}
.product .orig{text-decoration:line-through;font-size:7px;margin-top:28px;color:#777}
.product .stars{font-size:9px;color:#222}
.dots{position:absolute;left:386px;top:214px;display:flex;gap:9px}
.dots span{width:8px;height:8px;border-radius:50%;border:1px solid var(--blue)}
.dots .on{background:var(--blue)}
</style>
</head>
<body>

<div class="topbar">
  <div class="left"><span>1-800-555-0142</span><span class="sep">|</span><span>Chat</span><span class="sep">|</span><span>Contact Us</span><span class="sep">|</span><span>Credit Card</span></div>
  <div class="right"><span>Sign in / Create an account</span><span class="sep">|</span><span>Favorites</span><span class="sep">|</span><span>Order Status</span></div>
</div>

<header class="header">
  <div class="shipping">
    <svg width="20" height="15" viewBox="0 0 20 15"><rect x="0" y="1" width="12" height="9" fill="#333"/><path d="M12 4h4l3 3v3h-7z" fill="#333"/><circle cx="4" cy="12" r="2.2" fill="#333"/><circle cx="15" cy="12" r="2.2" fill="#333"/></svg>
    <div><div class="title">FREE SHIPPING NO MINIMUM</div><div class="line">To your door or to your store ›</div></div>
  </div>
  <div class="brand"><span class="mark"></span><span>LUCAS TORVI</span></div>
  <div class="search"><span>What can we help you find?</span><div class="btn"><svg width="12" height="12" viewBox="0 0 12 12"><circle cx="5" cy="5" r="3.5" fill="none" stroke="#fff" stroke-width="1.6"/><path d="M7.5 7.5l3 3" stroke="#fff" stroke-width="1.8"/></svg></div></div>
  <svg class="cart" width="26" height="24" viewBox="0 0 26 24"><path d="M7 9a6 6 0 0 1 12 0" fill="none" stroke="#444" stroke-width="2"/><path d="M1 9h24l-3 13H4z" fill="#444"/><path d="M8 12v7M13 12v7M18 12v7" stroke="#fff" stroke-width="1.5"/></svg>
</header>

<nav class="nav">
  <span class="item active" style="left:82px"><svg width="8" height="11" viewBox="0 0 8 11"><path d="M4 0a4 4 0 0 1 4 4c0 3-4 7-4 7S0 7 0 4a4 4 0 0 1 4-4z" fill="#4a8fc9"/><circle cx="4" cy="4" r="1.4" fill="#e9edf2"/></svg>Stores</span>
  <span class="bar" style="left:152px">|</span>
  <span class="item" style="left:186px"><svg width="10" height="10" viewBox="0 0 10 10"><circle cx="5" cy="5" r="4" fill="none" stroke="#555" stroke-dasharray="1.5 1"/></svg>Collections</span>
  <span class="bar" style="left:305px">|</span>
  <span class="item" style="left:336px"><svg width="11" height="10" viewBox="0 0 11 10"><rect x="1" y="3" width="9" height="7" fill="#333"/><rect x="0" y="2" width="11" height="2" fill="#333"/></svg>Fine Jewellary</span>
  <span class="bar" style="left:481px">|</span>
  <span class="item" style="left:513px">The World of Lucas Torvi</span>
  <span class="bar" style="left:726px">|</span>
  <span class="item" style="left:757px">Pearl bar</span>
</nav>

<section class="hero">
  <div class="wall" role="img" aria-label="Grey painted brick wall background"></div>
  <div class="model" role="img" aria-label="Model in a white shirt wearing layered dark pearl necklaces, a pearl ring and a pearl bracelet"></div>
  <h1 class="l1">CUSTOM DESIGN</h1>
  <h1 class="l2">DREAM NECKLACE</h1>
  <div class="band">
    <svg width="42" height="36" viewBox="0 0 42 36"><circle cx="11" cy="24" r="9" fill="#fff"/><circle cx="11" cy="22" r="4" fill="#4a8fc9"/><circle cx="30" cy="20" r="9" fill="#fff"/><circle cx="30" cy="18" r="4" fill="#4a8fc9"/><circle cx="12" cy="10" r="2.5" fill="#fff"/><circle cx="31" cy="6" r="2.5" fill="#fff"/></svg>
    <span>Earrings.....</span>
  </div>
  <div class="band-end"></div>
</section>

<div class="reviews">
  <span><span style="letter-spacing:1px">★★★★★</span><span class="score">4.7/5</span></span>
  <span><b>OVER 1,000,000+ REVIEWS</b> &amp; COUNTING</span>
  <span class="partner">REVORA</span>
</div>

<section class="deals">
  <div class="promo">
    <div class="kicker">LIMITED TIME ONLY</div>
    <div class="rule"></div>
    <h2>Dazzling<br>Deals</h2>
    <div class="note">LIMITED QUANTITIES<br>WHILE THEY LAST</div>
    <span class="cta">SHOP THE DEALS</span>
  </div>
  <div class="showcase" role="img" aria-label="Blue topaz halo ring, rose and white diamond cluster ring and square diamond stud earrings"></div>
  <div class="price" style="left:343px;top:90px"><sup>$</sup>99<sup>98</sup></div>
  <div class="was" style="left:353px;top:120px">WAS $219</div>
  <div class="price" style="left:648px;top:18px"><sup>$</sup>299<sup>98</sup></div>
  <div class="was" style="left:664px;top:48px">ORIG. $669</div>
  <div class="price" style="left:700px;top:124px"><sup>$</sup>399<sup>98</sup></div>
  <div class="was" style="left:710px;top:155px">WAS $549.99</div>
</section>

<section class="featured">
  <h3>Fetured Jewels</h3>
  <div class="product" style="left:78px"><div class="shot gold" role="img" aria-label="Gold name plate necklace"></div><div class="p">$239.00</div><div class="stars">★★★★☆ (6)</div></div>
  <div class="product" style="left:210px"><div class="shot silver" role="img" aria-label="Silver bangle with charm"></div><div class="orig">Orig. $38.00</div><div>Now $19.00</div></div>
  <div class="product" style="left:342px"><div class="shot black" role="img" aria-label="Black band ring"></div><div class="p">$229.00</div></div>
  <div class="product" style="left:475px"><div class="shot silver" role="img" aria-label="Diamond engagement ring"></div><div class="p">$529.00</div><div class="stars">★★★★☆ (9)</div></div>
  <div class="product" style="left:608px"><div class="shot rosegold" role="img" aria-label="Gold bangle with initial charm"></div><div class="orig">Orig. $32.00</div><div>Now $16.00</div></div>
  <div class="dots"><span class="on"></span><span></span></div>
</section>

</body>
</html>
```